Webdesign für Gemeinschaftspraxis (13820)
Zielgruppe
Die Website ist für eine fachärztliche Gemeinschaftspraxis, die sich aus Internisten, Betriebsmedizinern, Präventionsärzten, Kardiologen, Allgemeinmedizinern und Phlebologen zusammensetzt.
Die Zielgruppe sind bestehende Patienten sowie potentielle Patienten.
Die Website soll informativ sein.
Aufgabenstellung
Die Website soll in schlichten Farben gehalten sein, die zum Logo und zu den Fotos passen.
Die Website soll als kurzer, informativer Auftritt dienen
Die gelieferten Fotos sollen verwendet werden.
Es soll eine Onepage-Website werden, die so aufgebaut ist, wie die Website unter dem folgenden Link: https://www.kolbenfeld-portal.de/

```html
<!DOCTYPE html>
<html lang="de">
<head>
<meta charset="utf-8">
<title>Gemeinschaftspraxis Hollwede</title>
<link href="https://fonts.googleapis.com/css2?family=Work+Sans:wght@400;500;600;700&family=Karla:ital,wght@0,400;0,700;1,400&display=swap" rel="stylesheet">
<style>
:root{
  --navy:#1b2a5c;
  --navy-dark:#142148;
  --ink:#222838;
  --muted:#8a8f9c;
  --light:#f6f7f9;
  --card-fold:#c5cde0;
  --head-blue:#3b55b1;
  --time-blue:#6d87d7;
  --purple:#b45fd1;
  --slate:#7d8eaa;
  --pink:#ea9795;
  --lunch:#6b7ea5;
  --termin:#809ad0;
  --green:#6fc29f;
  --contact:#b7c1d5;
  --contact-light:#c7cfe0;
  --heading:"Work Sans",sans-serif;
  --body:"Karla",sans-serif;
}
*{box-sizing:border-box;margin:0;padding:0}
html,body{width:1200px;height:3965px;overflow:hidden}
body{position:relative;font-family:var(--body);color:var(--ink);background:#fff}
h1,h2,h3{font-weight:400}

/* Hero */
.hero{position:absolute;left:0;top:0;width:1200px;height:631px;overflow:hidden}
.hero-photo{position:absolute;inset:0;background:linear-gradient(135deg,#e9e6e1 0%,#f4f2ee 35%,#d9b48c 60%,#a97c52 78%,#6d5a4c 100%)}
.hero-shapes{position:absolute;inset:0}
.logo{position:absolute;left:111px;top:0;width:234px;height:151px;background:#fff;display:flex;align-items:center;justify-content:center;gap:10px;padding:0 12px}
.logo-mark{width:18px;height:18px;background:var(--navy);flex:none}
.logo-name{font-family:var(--heading);font-weight:600;font-size:15px;color:var(--navy);line-height:1.2}
.nav{position:absolute;left:492px;top:26px;width:708px;height:59px;background:var(--navy);display:flex;align-items:center;padding-left:47px;gap:30px}
.nav a{color:#fff;text-decoration:none;font-family:var(--heading);font-weight:600;font-size:11px;letter-spacing:.3px}
.hero-title{position:absolute;right:110px;top:448px;text-align:right;color:var(--navy);font-family:var(--heading)}
.hero-title h1{font-weight:700;font-size:43px;letter-spacing:1px;line-height:1}
.hero-title p{font-weight:400;font-size:31px;letter-spacing:1px;margin-top:6px;line-height:1}

/* Services */
.services{position:absolute;left:0;top:631px;width:1200px;height:743px;background:var(--light)}
.section-title{position:absolute;left:0;width:1200px;text-align:center;font-family:var(--heading);font-weight:400;font-size:31px;color:var(--navy);letter-spacing:1px}
.services-intro{position:absolute;left:0;top:124px;width:1200px;text-align:center;font-style:italic;font-size:14px;line-height:22px;color:#444}
.service{position:absolute;width:225px;height:188px;background:#fff;box-shadow:0 3px 8px rgba(0,0,0,.06);display:flex;align-items:center;justify-content:center;text-align:center;padding:0 10px}
.service svg{position:absolute;inset:0}
.service span{position:relative;font-family:var(--heading);font-weight:500;font-size:15px;line-height:26px;color:var(--ink);letter-spacing:.3px}
.service.active{background:var(--navy);flex-direction:column;gap:24px;border:1px solid #3a4b85}
.service.active span{color:#fff;text-decoration:underline;text-underline-offset:3px}
.service-more{position:relative;border:1px solid #fff;color:#fff;font-family:var(--heading);font-weight:600;font-size:10px;padding:6px 8px;letter-spacing:.3px}
.dots{position:absolute;top:652px;left:577px;display:flex;gap:7px}
.dots i{width:9px;height:9px;background:#8d9bc4;display:block}
.dots i.on{background:var(--navy)}

/* Doctors */
.doctors{position:absolute;left:0;top:1374px;width:1200px;height:584px;background:#fff}
.doctor{position:absolute;top:120px;width:309px;height:390px;background:#fff;box-shadow:0 3px 12px rgba(0,0,0,.08);text-align:center}
.doctor-photo{height:223px}
.doctor h3{font-family:var(--heading);font-weight:500;font-size:16px;margin-top:30px;color:var(--ink)}
.doctor small{display:block;font-size:11px;color:var(--muted);margin-top:8px;letter-spacing:.3px}
.btn{display:inline-block;background:var(--navy);color:#fff;font-family:var(--heading);font-weight:600;font-size:11px;letter-spacing:.3px}
.doctor .btn{width:172px;height:39px;line-height:39px;margin-top:14px}

/* Hours */
.hours{position:absolute;left:0;top:1958px;width:1200px;height:900px;background:linear-gradient(90deg,#d8dadf 0%,#eeeff1 25%,#f3f3f4 60%,#d4d6da 100%)}
.hours .section-title{top:44px}
.schedule{position:absolute;left:111px;top:98px;width:978px;border-collapse:collapse;font-family:var(--heading);font-size:14px;color:#fff}
.schedule th{background:var(--head-blue);height:40px;text-align:left;padding-left:17px;font-weight:600;font-size:13px;border-right:1px solid rgba(255,255,255,.35)}
.schedule td{height:64.5px;vertical-align:top;padding:15px 0 0 18px;line-height:19px;font-weight:500;border-right:1px solid rgba(255,255,255,.35);border-top:1px solid rgba(255,255,255,.35)}
.schedule td.time{background:var(--time-blue);width:163px;padding-left:22px}
.schedule td.blood{background:var(--purple)}
.schedule td.free{background:var(--slate)}
.schedule td.visit{background:var(--pink)}
.schedule td.lunch{background:var(--lunch)}
.schedule td.appt{background:var(--termin)}
.schedule td.open{background:var(--green)}

/* Team */
.team{position:absolute;left:0;top:2858px;width:1200px;height:631px;background:#fff}
.team-photo{position:absolute;left:115px;top:110px;width:395px;height:521px;z-index:0;background:radial-gradient(ellipse at 45% 35%,#e7c4a8 0%,#c79b7a 26%,#3157b8 55%,#dfe5f2 85%,#fff 100%)}
.team-copy{position:absolute;left:531px;top:0;width:558px;height:631px;z-index:1}
.team-title{position:absolute;left:0;top:90px;font-family:var(--heading);font-weight:400;font-size:31px;line-height:38px;color:var(--navy);letter-spacing:1px;white-space:nowrap}
.team-line{position:absolute;left:268px;top:113px;width:208px;height:1px;background:#dde1ea}
.team-arrows{position:absolute;left:489px;top:97px;display:flex;gap:2px}
.team-arrows span{width:33px;height:32px;display:flex;align-items:center;justify-content:center}
.team-arrows .prev{background:var(--navy)}
.team-arrows .next{background:#e3e6ec}
.team-name{position:absolute;left:0;top:165px;font-family:var(--heading);font-weight:400;font-size:20px;line-height:24px;color:#333;letter-spacing:.5px}
.team-role{position:absolute;left:0;top:193px;font-family:var(--body);font-style:italic;font-size:11px;line-height:14px;color:#555}
.team-text{position:absolute;left:0;top:237px;width:558px;font-size:13px;line-height:22px;color:#666}
.team-text p{margin-bottom:22px}

/* Contact & footer */
.contact{position:absolute;left:0;top:3489px;width:1200px;height:476px;background:var(--contact);overflow:hidden}
.contact-shapes{position:absolute;inset:0}
.contact .section-title{top:68px;color:var(--ink)}
.field{position:absolute;top:121px;width:217px;height:49px;background:#9eabc5;color:#e8ecf5;font-style:italic;font-size:12px;padding:18px 17px;letter-spacing:.5px}
.submit{position:absolute;left:829px;top:121px;width:217px;height:49px;line-height:49px;text-align:center;font-size:14px;letter-spacing:1px}
.divider{position:absolute;left:222px;top:215px;width:756px;height:1px;background:#9aa7c2}
.footer-logo{position:absolute;left:191px;top:259px;width:230px;height:136px;display:flex;align-items:center;justify-content:center;gap:10px}
.footer-info{position:absolute;font-size:12px;color:var(--ink);display:flex;align-items:center;gap:10px;font-family:var(--heading)}
.footer-info svg{flex:none}
.footer-copy{position:absolute;font-size:12px;color:var(--ink);font-family:var(--heading);white-space:nowrap}
</style>
</head>
<body>

<header class="hero">
  <div class="hero-photo" role="img" aria-label="Foto des hellen Empfangsbereichs der Praxis mit Holztresen und Blumen"></div>
  <svg class="hero-shapes" width="1200" height="631" viewBox="0 0 1200 631">
    <polygon points="0,185 500,631 0,631" fill="#1b2a5c"/>
  </svg>
  <div class="logo"><span class="logo-mark"></span><span class="logo-name">Gemeinschaftspraxis Hollwede</span></div>
  <nav class="nav">
    <a>HOME</a><a>DIENSTLEISTUNGEN</a><a>UNSER TEAM</a><a>ÖFFNUNGSZEITEN</a><a>KONTAKTIERE UNS</a>
  </nav>
  <div class="hero-title">
    <h1>SED UT PERSPICIATIS</h1>
    <p>UNDE OMNIS ISTE NATUS</p>
  </div>
</header>

<section class="services">
  <h2 class="section-title" style="top:80px">UNSERE DIENSTLEISTUNGEN</h2>
  <p class="services-intro">Nemo enim ipsam voluptatem quia voluptas sit aspernatur aut odit aut fugit, sed quia<br>consequuntur magni dolores eos qui ratione voluptatem sequi nesciunt.</p>

  <div class="service" style="left:120px;top:204px">
    <svg width="225" height="188"><polygon points="0,0 62,0 0,45" fill="#c5cde0"/><polygon points="225,120 225,188 168,188" fill="#c5cde0"/></svg>
    <span>GESUNDHEITSVORSORGE<br>/PRÄVENTION/<br>GESUNDHEITS-CHECK-UP</span>
  </div>
  <div class="service" style="left:361px;top:204px">
    <svg width="225" height="188"><polygon points="0,0 62,0 0,45" fill="#c5cde0"/><polygon points="225,120 225,188 168,188" fill="#c5cde0"/></svg>
    <span>IMPFUNGEN UND<br>REISEIMPFUNGEN</span>
  </div>
  <div class="service active" style="left:612px;top:204px">
    <svg width="225" height="188"><polygon points="0,0 62,0 0,45" fill="#c5cde0"/></svg>
    <span>MÄNNERVORSORGE</span>
    <div class="service-more">MEHR INFORMATIONEN</div>
  </div>
  <div class="service" style="left:854px;top:204px">
    <svg width="225" height="188"><polygon points="0,0 62,0 0,45" fill="#c5cde0"/><polygon points="225,120 225,188 168,188" fill="#c5cde0"/></svg>
    <span>DIABETES<br>MELLITUS</span>
  </div>

  <div class="service" style="left:120px;top:418px">
    <svg width="225" height="188"><polygon points="0,0 62,0 0,45" fill="#c5cde0"/><polygon points="225,120 225,188 168,188" fill="#c5cde0"/></svg>
    <span>PSYCHOSOMATISCHE<br>GRUNDVERSORGUNG</span>
  </div>
  <div class="service" style="left:361px;top:418px">
    <svg width="225" height="188"><polygon points="0,0 62,0 0,45" fill="#c5cde0"/><polygon points="225,120 225,188 168,188" fill="#c5cde0"/></svg>
    <span>KORONARE<br>HERZERKRANKUNG<br>(KHK)</span>
  </div>
  <div class="service" style="left:612px;top:418px">
    <svg width="225" height="188"><polygon points="0,0 62,0 0,45" fill="#c5cde0"/><polygon points="225,120 225,188 168,188" fill="#c5cde0"/></svg>
    <span>ASTHMA<br>BRONCHIAL</span>
  </div>
  <div class="service" style="left:854px;top:418px">
    <svg width="225" height="188"><polygon points="0,0 62,0 0,45" fill="#c5cde0"/><polygon points="225,120 225,188 168,188" fill="#c5cde0"/></svg>
    <span>PALLIATIVERSORGUNG</span>
  </div>

  <div class="dots"><i></i><i class="on"></i><i></i></div>
</section>

<section class="doctors">
  <h2 class="section-title" style="top:58px">UNSERE ÄRZTE</h2>
  <article class="doctor" style="left:111px">
    <div class="doctor-photo" role="img" aria-label="Porträtfoto der Ärztin vor Ziegelwand" style="background:linear-gradient(135deg,#a0543f,#6b3a2d 45%,#c8886a)"></div>
    <h3>Marie Kessler</h3><small>Vice President</small>
    <span class="btn">MEHR INFORMATIONEN</span>
  </article>
  <article class="doctor" style="left:446px">
    <div class="doctor-photo" role="img" aria-label="Porträtfoto des Arztes mit Brille vor grauem Hintergrund" style="background:linear-gradient(135deg,#c9ced2,#aeb5b8 50%,#5e7e77)"></div>
    <h3>Jonas.R</h3><small>Vice President</small>
    <span class="btn">MEHR INFORMATIONEN</span>
  </article>
  <article class="doctor" style="left:780px">
    <div class="doctor-photo" role="img" aria-label="Porträtfoto des Arztes im Pullover vor Stadtkulisse" style="background:linear-gradient(135deg,#8c7f78,#b9b2ad 50%,#1e2436)"></div>
    <h3>Lukas Brandt</h3><small>Vice President</small>
    <span class="btn">MEHR INFORMATIONEN</span>
  </article>
</section>

<section class="hours" role="img" aria-label="Hintergrund: blasses Foto des Praxisgebäudes mit Bäumen">
  <h2 class="section-title">ÖFFNUNGSZEITEN</h2>
  <table class="schedule">
    <tr><th>ZEIT</th><th>MONTAG</th><th>DIENSTAG</th><th>MITTWOCH</th><th>DONNERSTAG</th><th>FREITAG</th></tr>
    <tr><td class="time">AB 7:30</td><td class="blood">Blutentnahme/<br>Ultraschall</td><td class="blood">Blutentnahme/<br>Ultraschall</td><td class="blood">Blutentnahme/<br>Ultraschall</td><td class="blood">Blutentnahme/<br>Ultraschall</td><td class="blood">Blutentnahme/<br>Ultraschall</td></tr>
    <tr><td class="time">8:00-9:30</td><td class="free">Freie<br>Sprechstunde</td><td class="free">Freie<br>Sprechstunde</td><td class="free">Freie<br>Sprechstunde</td><td class="free">Freie<br>Sprechstunde</td><td class="free">Freie<br>Sprechstunde</td></tr>
    <tr><td class="time">9:00-10:00</td><td class="free">Freie<br>Sprechstunde</td><td class="free">Freie<br>Sprechstunde</td><td class="free">Freie<br>Sprechstunde</td><td class="free">Freie<br>Sprechstunde</td><td class="free">Freie<br>Sprechstunde</td></tr>
    <tr><td class="time">10:00-11:00</td><td class="free">Freie<br>Sprechstunde</td><td class="free">Freie<br>Sprechstunde</td><td class="free">Freie<br>Sprechstunde</td><td class="free">Freie<br>Sprechstunde</td><td class="free">Freie<br>Sprechstunde</td></tr>
    <tr><td class="time">11:00-12:00</td><td class="free">Freie<br>Sprechstunde</td><td class="free">Freie<br>Sprechstunde</td><td class="free">Freie<br>Sprechstunde</td><td class="free">Freie<br>Sprechstunde</td><td class="free">Freie<br>Sprechstunde</td></tr>
    <tr><td class="time">12:00-13:00</td><td class="visit">Hausbesuche</td><td class="visit">Hausbesuche</td><td class="visit">Hausbesuche</td><td class="visit">Hausbesuche</td><td class="visit">Hausbesuche</td></tr>
    <tr><td class="time">13:00-14:00</td><td class="lunch">Mittagspause</td><td class="lunch">Mittagspause</td><td class="lunch">Mittagspause</td><td class="lunch">Mittagspause</td><td class="lunch">Mittagspause</td></tr>
    <tr><td class="time">14:00-15:30</td><td class="lunch">Mittagspause</td><td class="lunch">Mittagspause</td><td class="lunch">Mittagspause</td><td class="lunch">Mittagspause</td><td class="lunch">Mittagspause</td></tr>
    <tr><td class="time">15:30-16:00</td><td class="appt">Termin-<br>sprechstunde</td><td class="appt">Termin-<br>sprechstunde</td><td class="appt">Termin-<br>sprechstunde</td><td class="appt">Termin-<br>sprechstunde</td><td class="appt">Termin-<br>sprechstunde</td></tr>
    <tr><td class="time">16:00-17:00</td><td class="open">Freie<br>Sprechstunde</td><td class="open">Freie<br>Sprechstunde</td><td class="open"></td><td class="open">Freie<br>Sprechstunde</td><td class="open"></td></tr>
    <tr><td class="time">17:00-18:00</td><td class="open">Freie<br>Sprechstunde</td><td class="open">Freie<br>Sprechstunde</td><td class="open"></td><td class="open">Freie<br>Sprechstunde</td><td class="open"></td></tr>
  </table>
</section>

<section class="team">
  <div class="team-photo" role="img" aria-label="Foto der Praxisleiterin in blauer Bluse mit verschränkten Armen"></div>
  <div class="team-copy">
    <h2 class="team-title">TRIFF DAS TEAM</h2>
    <div class="team-line"></div>
    <div class="team-arrows">
      <span class="prev"><svg width="10" height="12" viewBox="0 0 10 12"><polyline points="7,1 2,6 7,11" fill="none" stroke="#fff" stroke-width="2"/></svg></span>
      <span class="next"><svg width="10" height="12" viewBox="0 0 10 12"><polyline points="3,1 8,6 3,11" fill="none" stroke="#fff" stroke-width="2"/></svg></span>
    </div>
    <h3 class="team-name">Helena S. Vogt</h3>
    <div class="team-role">CEO</div>
    <div class="team-text">
      <p>But I must explain to you how all this mistaken idea of denouncing pleasure and praising pain was born and I will give you a complete account of the system, and expound the actual teachings of the great explorer of the truth, the master-builder of human happiness.</p>
      <p>No one rejects, dislikes, or avoids pleasure itself, because it is pleasure, but because those who do not know how to pursue pleasure rationally encounter consequences that are extremely painful. Nor again is there anyone who loves or pursues or desires to obtain pain of itself, because it is pain, but because occasionally circumstances occur in which toil and pain can procure him some great pleasure. To take a trivial example, which of us ever undertakes laborious physical exercise, except to obtain some advantage from it.</p>
      <p>But who has any right to find fault with a man who chooses to enjoy a pleasure that has no annoying consequences, or one who avoids a pain that produces.</p>
    </div>
  </div>
</section>

<footer class="contact">
  <svg class="contact-shapes" width="1200" height="476" viewBox="0 0 1200 476">
    <polygon points="0,0 1200,0 1200,160 0,260" fill="#c0c9db"/>
    <polygon points="0,260 1200,160 1200,476 0,476" fill="#b2bdd3"/>
  </svg>
  <h2 class="section-title">KONTAKT FORMULAR</h2>
  <div class="field" style="left:154px">Name:</div>
  <div class="field" style="left:378px">Telefon:</div>
  <div class="field" style="left:603px">Telefon:</div>
  <span class="btn submit">EINREICHEN</span>
  <div class="divider"></div>

  <div class="footer-logo"><span class="logo-mark"></span><span class="logo-name">Gemeinschaftspraxis Hollwede</span></div>

  <div class="footer-info" style="left:517px;top:288px">
    <svg width="12" height="14" viewBox="0 0 12 14"><path d="M6 0a5 5 0 0 1 5 5c0 4-5 9-5 9S1 9 1 5a5 5 0 0 1 5-5z" fill="#1b2a5c"/><circle cx="6" cy="5" r="2" fill="#b7c1d5"/></svg>
    Am Lindenhof 14, 48100 Hollwede</div>
  <div class="footer-info" style="left:517px;top:313px">
    <svg width="13" height="12" viewBox="0 0 13 12"><rect x="0" y="3" width="13" height="9" fill="#1b2a5c"/><rect x="2" y="0" width="9" height="3" fill="#1b2a5c"/></svg>
    04521 7738 191</div>
  <div class="footer-info" style="left:786px;top:288px">
    <svg width="13" height="13" viewBox="0 0 13 13"><path d="M3 0l2 3-1.5 1.5a8 8 0 0 0 5 5L10 8l3 2-1.5 2.5C6 13 0 7 .5 1.5z" fill="#1b2a5c"/></svg>
    04521 7738 190</div>
  <div class="footer-info" style="left:786px;top:313px">
    <svg width="13" height="10" viewBox="0 0 13 10"><rect x=".5" y=".5" width="12" height="9" fill="none" stroke="#1b2a5c"/><polyline points=".5,.5 6.5,5.5 12.5,.5" fill="none" stroke="#1b2a5c"/></svg>
    info@praxis-hollwede.example</div>
  <div class="footer-copy" style="left:517px;top:354px">Copyright © 2019. Gemeinschaftspraxis Hollwede</div>
  <div class="footer-copy" style="left:812px;top:354px">Datenschutz-Bestimmungen</div>
  <div class="footer-copy" style="left:517px;top:380px">Alle Rechte vorbehalten.</div>
</footer>

</body>
</html>
```